Healthy lifestyle Influencer business card

I need your creativity to have a business card that I can leave in all the restaurants, hotels and spas I visit to inform them that I am an influencer specializing in the wellness sector and that I will write a review about them. You can use my instagram photos Lunavivo27 or on my website www.piattileggerisani.it. I would like my business card to impress with its creativity! thank you very much!

Contact Information for Business Card

siteweb, instagram, phone number

Font styles to use
Decorative
Script

Colors
0094D4
00A9DD
6FCCEA
C7EBF8
E9F6FB
59FF00
82FF00
B8FF75
E3FFCB
F4FFEA
FFC000
F8CF3A
FAE287
FDF2CF
FEFAEE
F0912C
F2A743
F7CA91
FBE8D2
FDF5EE
EE7325
F08F49
F5BC92
FAE3D3
FDF4ED
EB3D1F
EC4F4E
F09395
F8D3D4
FCEDEE
E54698
E96AAD
F1A4CE
F9D9EA
FCEFF6

Requirements
Nice to have
• creativity

```html
<!DOCTYPE html>
<html lang="it">
<head>
<meta charset="utf-8">
<title>Luna Vivo Chef – Biglietto da visita</title>
<link href="https://fonts.googleapis.com/css2?family=Josefin+Sans:wght@300;600&family=Sacramento&display=swap" rel="stylesheet">
<style>
  :root {
    --backdrop: #f0e4e2;
    --card: #ffffff;
    --ink: #5a5a5a;
    --ink-soft: #6b6b6b;
    --mint: #9dcbba;
    --mint-light: #b6d6cc;
    --mint-deep: #9bbbb1;
    --mint-text: #9fcfbd;
  }
  * { margin: 0; padding: 0; box-sizing: border-box; }
  html, body { width: 1200px; height: 1200px; overflow: hidden; }
  body { background: var(--backdrop); position: relative; font-family: "Josefin Sans", sans-serif; }

  .card {
    position: absolute;
    left: 268px;
    width: 654px;
    height: 373px;
    background: var(--card);
    overflow: hidden;
  }
  .card--front { top: 172px; }
  .card--back { top: 644px; }

  .front-brand {
    position: absolute;
    left: 0; right: 0;
    top: 140px;
    text-align: center;
  }
  .brand-name {
    font-weight: 600;
    font-size: 50px;
    color: var(--ink);
    letter-spacing: 1px;
    line-height: 1;
  }
  .brand-tagline {
    margin-top: 22px;
    font-weight: 600;
    font-size: 21px;
    color: var(--ink-soft);
  }

  .waves { position: absolute; left: 0; top: 0; width: 654px; height: 373px; }

  .owner-name {
    position: absolute;
    left: 100px;
    top: 42px;
    font-family: "Sacramento", cursive;
    font-size: 42px;
    color: var(--mint-text);
    letter-spacing: 2px;
    white-space: nowrap;
  }

  .contacts { position: absolute; left: 340px; top: 135px; list-style: none; }
  .contact {
    display: flex;
    align-items: center;
    height: 22px;
    margin-bottom: 23px;
    font-weight: 300;
    font-size: 19px;
    color: var(--mint-text);
    letter-spacing: 0.5px;
    white-space: nowrap;
  }
  .contact-icon {
    width: 18px; height: 18px;
    margin-right: 13px;
    flex: none;
  }

  .back-brand {
    position: absolute;
    left: 24px;
    top: 280px;
    width: 180px;
    text-align: center;
  }
  .back-brand .brand-name { font-size: 17px; letter-spacing: 0.5px; }
  .back-brand .brand-tagline { margin-top: 6px; font-size: 8px; color: var(--ink); }
</style>
</head>
<body>

  <section class="card card--front">
    <div class="front-brand">
      <div class="brand-name">Luna Vivo Chef</div>
      <div class="brand-tagline">Leggeri con i sapori che ami</div>
    </div>
  </section>

  <section class="card card--back">
    <svg class="waves" viewBox="0 0 611 348" preserveAspectRatio="none" aria-hidden="true">
      <path fill="var(--mint)" d="M0,118 C130,105 230,140 318,232 C380,297 480,268 611,250 L611,348 L0,348 Z"/>
      <path fill="var(--mint-light)" d="M0,165 C140,155 240,185 330,250 C400,295 480,292 611,270 L611,348 L0,348 Z"/>
      <path fill="var(--mint-deep)" d="M0,202 C155,195 258,230 345,265 C420,295 505,300 611,287 L611,348 L0,348 Z"/>
    </svg>

    <div class="owner-name">Luna Ferretti Vivaldi</div>

    <ul class="contacts">
      <li class="contact">
        <svg class="contact-icon" viewBox="0 0 18 18" aria-hidden="true">
          <circle cx="9" cy="9" r="9" fill="var(--mint)"/>
          <path fill="#fff" d="M6.2 4.6c.4-.2.8 0 1 .4l.8 1.7c.2.4.1.8-.2 1l-.7.6c.5 1.1 1.3 2 2.4 2.5l.6-.7c.3-.3.7-.4 1-.2l1.7.8c.4.2.5.6.4 1l-.4 1.1c-.2.4-.6.6-1 .6-3.4-.3-6.2-3.1-6.5-6.5 0-.4.2-.8.6-1z"/>
        </svg>
        008 512 307 9914
      </li>
      <li class="contact">
        <svg class="contact-icon" viewBox="0 0 18 18" aria-hidden="true">
          <circle cx="9" cy="9" r="9" fill="var(--mint)"/>
          <circle cx="9" cy="9" r="4.5" fill="none" stroke="#fff" stroke-width="1"/>
          <path d="M4.5 9h9M9 4.5v9" stroke="#fff" stroke-width="1"/>
        </svg>
        www.piattileggerisani.it
      </li>
      <li class="contact">
        <svg class="contact-icon" viewBox="0 0 18 18" aria-hidden="true">
          <circle cx="9" cy="9" r="9" fill="var(--mint)"/>
        </svg>
        @lunavivo27
      </li>
    </ul>

    <div class="back-brand">
      <div class="brand-name">Luna Vivo Chef</div>
      <div class="brand-tagline">Leggeri con i sapori che ami</div>
    </div>
  </section>

</body>
</html>
```